Business Cards Needed for Innovative Healthcare Marketing Company

We are a marketing company focused on healthcare. Our company is all about rebranding yourself renewing your image and generating results. The phoenix stands for "reborn" or "rising" which we provide new brands for our clients we take their old brands and renew it with creativity and innovation. I am looking for a business card with color dimension. I have attached an example of a card I think has the look and feel of what I am trying to accomplish. I like that the card example has black and grey font colors, I like the font placement and the small logo, I really like the use of the colors on the right those are the colors of my logo. My logo is phoenix so maybe incorporating flames similar to that design. I would like the back a solid color maybe red with an opaque version of the logo and website. As a marketing company I am always open to creative liberty!

Target Market(s)

Doctors and business professionals.

Industry/Entity Type

Marketing

Contact Information for Business Card

Velmora Health Care Marketing
Dana Prewitt- CEO
#(407)555-0172
email-dana@velmora.com
website- velmora.com

Font styles to use
Sans Serif

Colors
ec1f27
f37122
ffc214
fbed22
fbf289
f04a50

Requirements
Must have
• The logo and required information
Nice to have
• icons by the information
Should not have
• child like font

```html
<!DOCTYPE html>
<html lang="en">
<head>
<meta charset="utf-8">
<title>Velmora Health Care Marketing – Business Cards</title>
<link rel="stylesheet" href="https://fonts.googleapis.com/css2?family=Montserrat:wght@300;400;500;700&display=swap">
<style>
  :root {
    --backdrop: #2b2b2b;
    --card: #050505;
    --white: #ffffff;
    --soft-white: #e8e8e8;
    --orange: #f39a1e;
    --flame: #f37122;
    --red: #ec1f27;
    --rule: #6b2b23;
  }
  * { margin: 0; padding: 0; box-sizing: border-box; }
  html, body {
    width: 1200px; height: 900px; overflow: hidden;
    background: var(--backdrop);
    font-family: "Montserrat", Arial, sans-serif;
  }
  .canvas {
    width: 1200px; height: 900px;
    display: flex; flex-direction: column; align-items: center; justify-content: center;
    gap: 60px;
  }
  .card {
    width: 630px; height: 360px;
    background: var(--card);
    border-radius: 22px;
    position: relative;
    overflow: hidden;
    color: var(--white);
  }

  /* Front */
  .front { display: flex; flex-direction: column; align-items: center; justify-content: center; }
  .brand { display: flex; align-items: center; gap: 18px; margin-top: -20px; }
  .brand-dot {
    width: 34px; height: 34px; border-radius: 50%;
    background: var(--flame);
  }
  .brand-name {
    font-weight: 300; font-size: 58px; letter-spacing: 4px; line-height: 1;
    color: var(--white);
  }
  .brand-rule {
    width: 300px; height: 1px; background: var(--rule);
    margin: 12px 0 10px 52px;
  }
  .tagline {
    font-weight: 300; font-size: 17px; letter-spacing: 2px;
    color: var(--soft-white); margin-left: 52px;
  }
  .front-web {
    position: absolute; bottom: 48px; left: 0; right: 0;
    text-align: center; font-size: 21px; font-weight: 400; letter-spacing: 0.5px;
  }

  /* Back */
  .back { display: flex; align-items: center; }
  .back-brand {
    width: 320px; display: flex; align-items: center; justify-content: center; gap: 12px;
  }
  .back-brand .brand-dot { width: 26px; height: 26px; }
  .back-brand .brand-name { font-size: 38px; letter-spacing: 3px; }
  .divider {
    width: 1px; height: 140px;
    background: linear-gradient(to bottom, rgba(255,255,255,0), #d9d9d9 40%, #8a5a3a);
  }
  .contact { padding-left: 48px; }
  .person-name {
    font-weight: 700; font-size: 25px; letter-spacing: 1px; color: var(--orange);
  }
  .person-title {
    font-size: 16px; font-weight: 400; margin: 4px 0 12px 18px; letter-spacing: 1px;
  }
  .contact-list { list-style: none; margin-left: 18px; }
  .contact-list li {
    display: flex; align-items: center; gap: 10px;
    font-size: 16px; line-height: 26px; color: var(--white);
  }
  .contact-list svg { width: 12px; height: 12px; flex: none; }
</style>
</head>
<body>
<main class="canvas">

  <section class="card front" aria-label="Card front">
    <div class="brand">
      <span class="brand-dot"></span>
      <span class="brand-name">VELMORA</span>
    </div>
    <div class="brand-rule"></div>
    <p class="tagline">HEALTHCARE MARKETING</p>
    <p class="front-web">www.velmora.com</p>
  </section>

  <section class="card back" aria-label="Card back">
    <div class="back-brand">
      <span class="brand-dot"></span>
      <span class="brand-name">VELMORA</span>
    </div>
    <div class="divider"></div>
    <div class="contact">
      <h1 class="person-name">DANA PREWITT</h1>
      <p class="person-title">CEO</p>
      <ul class="contact-list">
        <li>
          <svg viewBox="0 0 24 24" aria-hidden="true"><path fill="#f39a1e" d="M6.6 10.8a15.1 15.1 0 0 0 6.6 6.6l2.2-2.2c.3-.3.7-.4 1-.2 1.1.4 2.3.6 3.6.6.6 0 1 .4 1 1V20c0 .6-.4 1-1 1A17 17 0 0 1 3 4c0-.6.4-1 1-1h3.5c.6 0 1 .4 1 1 0 1.3.2 2.5.6 3.6.1.3 0 .7-.2 1z"/></svg>
          (407)555-0172
        </li>
        <li>
          <svg viewBox="0 0 24 24" aria-hidden="true"><rect x="2" y="5" width="20" height="14" rx="1.5" fill="none" stroke="#f39a1e" stroke-width="2.4"/><path d="M3 6l9 7 9-7" fill="none" stroke="#f39a1e" stroke-width="2.4"/></svg>
          dana@velmora.com
        </li>
        <li>
          <svg viewBox="0 0 24 24" aria-hidden="true"><circle cx="12" cy="12" r="9.5" fill="none" stroke="#f39a1e" stroke-width="2.4"/><path d="M2.5 12h19M12 2.5c3 3 3 16 0 19M12 2.5c-3 3-3 16 0 19" fill="none" stroke="#f39a1e" stroke-width="2"/></svg>
          www.velmora.com
        </li>
      </ul>
    </div>
  </section>

</main>
</body>
</html>
```